Design a Trade Show Banner

We're a cloud security company launching two new products called Kelvaro Grantwise and Kelvaro QRX. (Feel free to get some details from our website). Also feel free to leave a wireframe/photo for Zentab and web/monitor screenshots, and I will get updated web/monitor screenshots soon.

We will have a table at MVRQ in Austin and need a 2x7 (two foot by seven foot vertical) pop-up banner, like this: http://www.tramhoistbanners.com/

The logo on our website is not currently in the correct colors.. (please see attached file). We prefer the grey and yellow logo out of the four in the attached Illustrator file (lower-right). (Please don't use the PNG, that's just for looks - if you need other formats for the vector file, let me know.)

Image size should be:
84" (213.36 cm) + 4" (10.16cm) plain white =
88"/223.52cm total length, and
24" (60.96cm) wide.

This is for a tradeshow, so go big and colorful!

Thanks!

```html
<!DOCTYPE html>
<html lang="en">
<head>
<meta charset="utf-8">
<title>Kelvaro – Trade Show Banner</title>
<link rel="stylesheet" href="https://fonts.googleapis.com/css2?family=Exo+2:wght@300;400;800&family=Sacramento&display=swap">
<style>
  :root {
    --white: #ffffff;
    --orange: #f5a31c;
    --grey: #7a7a7a;
    --ink: #2b2b2b;
    --leaf-dark: #4f6a3c;
    --leaf-light: #c9d6b8;
  }
  html, body { margin: 0; padding: 0; overflow: hidden; }
  .banner {
    position: relative;
    width: 1200px;
    height: 4196px;
    background: var(--white);
    overflow: hidden;
    font-family: "Exo 2", sans-serif;
  }
  .banner__art { position: absolute; inset: 0; }
  .brand {
    position: absolute;
    left: 0; right: 0;
    top: 300px;
    text-align: center;
  }
  .brand__name {
    margin: 0;
    font-weight: 800;
    font-size: 230px;
    line-height: 1;
    color: var(--grey);
    letter-spacing: -4px;
  }
  .brand__tagline {
    margin: 6px 0 0;
    font-weight: 400;
    font-size: 38px;
    color: var(--orange);
    letter-spacing: 1px;
  }
  .brand__url {
    margin: 70px 0 0;
    font-weight: 400;
    font-size: 72px;
    color: var(--ink);
  }
  .message {
    position: absolute;
    left: 84px;
    top: 3440px;
    margin: 0;
    font-weight: 300;
    font-size: 140px;
    line-height: 190px;
    color: var(--ink);
  }
  .slogan {
    position: absolute;
    left: 60px;
    top: 3900px;
    margin: 0;
    font-family: "Sacramento", cursive;
    font-size: 200px;
    line-height: 1;
    color: var(--ink);
  }
</style>
</head>
<body>
<main class="banner">
  <svg class="banner__art" width="1200" height="4196" viewBox="0 0 1200 4196">
    <defs>
      <linearGradient id="park-tones" x1="0" y1="0" x2="1" y2="1">
        <stop offset="0" stop-color="var(--leaf-dark)"/>
        <stop offset="0.5" stop-color="var(--leaf-light)"/>
        <stop offset="1" stop-color="var(--leaf-dark)"/>
      </linearGradient>
    </defs>
    <path class="photo-area" role="img" aria-label="Photo: a young woman in a white dress sits on the grass in a sunny park working on a laptop"
          d="M0,2280 Q520,1320 1200,1090 L1200,3140 Q620,3560 0,3190 Z" fill="url(#park-tones)"/>
    <path class="swoosh-band" d="M0,1230 Q520,840 1200,650 L1200,1090 Q520,1320 0,2280 Z" fill="var(--orange)"/>
    <path class="footer-band" d="M0,3190 Q620,3560 1200,3140 L1200,4196 L0,4196 Z" fill="var(--orange)"/>

    <g class="feature-icons" fill="none" stroke="var(--white)" stroke-width="10" stroke-linejoin="round">
      <g class="icon-play" transform="translate(130,1680) rotate(-14)">
        <rect x="-120" y="-90" width="240" height="180" rx="30"/>
        <path d="M-25,-40 L40,0 L-25,40 Z" fill="var(--white)" stroke="none"/>
      </g>
      <g class="icon-tick" transform="translate(330,1385) rotate(-22)">
        <rect x="-130" y="-85" width="260" height="170"/>
        <path d="M-40,-5 L-5,35 L55,-55" stroke-width="16"/>
      </g>
      <g class="icon-mail" transform="translate(600,1150) rotate(-24)">
        <rect x="-125" y="-80" width="250" height="160"/>
        <path d="M-125,-80 L0,20 L125,-80"/>
      </g>
      <g class="icon-book" transform="translate(905,990) rotate(-14)">
        <path d="M-120,70 L-120,-60 Q-60,-85 0,-55 Q60,-85 120,-60 L120,70 Q60,45 0,70 Q-60,45 -120,70 Z"/>
        <path d="M0,-55 L0,70"/>
        <path d="M-130,85 L130,85"/>
      </g>
      <g class="icon-folder" transform="translate(1140,870) rotate(-14)">
        <path d="M-90,-55 L-40,-55 L-25,-35 L90,-35 L90,60 L-90,60 Z"/>
        <path d="M-90,60 L-70,-10 L110,-10 L90,60"/>
      </g>
    </g>
  </svg>

  <header class="brand">
    <h1 class="brand__name">Kelvaro</h1>
    <p class="brand__tagline">USER MANAGEMENT FOR THE CLOUD</p>
    <p class="brand__url">kelvaro.com</p>
  </header>

  <p class="message">with<br>secured data</p>
  <p class="slogan">Live your life!</p>
</main>
</body>
</html>
```